Veracor Systems
Business Cards
Veracor Systems - Information Technology
Creative Brief
Professional
Martin Osgood
Vice President
Veracor IT Systems Harbourline Tower 482 Dunmore Ave East,Suite 3100 Toronto ON, M4R 2T7
martin.osgood@veracorsystems-example.ca
www.veracorsystems-example.ca

```html
<!DOCTYPE html>
<html lang="en">
<head>
<meta charset="utf-8">
<title>Veracor Systems – Stationery Concepts</title>
<link href="https://fonts.googleapis.com/css2?family=Exo+2:wght@700&family=Open+Sans:wght@400;600&display=swap" rel="stylesheet">
<style>
:root{
  --bg:#3a3b3d;
  --bg-dark:#2c2d2f;
  --paper:#ffffff;
  --paper-shade:#eef1f4;
  --blue:#1f9fd8;
  --blue-deep:#1178b0;
  --blue-pale:#d6eef9;
  --ink:#4a4d52;
  --label:#c9cbce;
  --env-dark:#5b5d61;
}
*{margin:0;padding:0;box-sizing:border-box}
html,body{width:1200px;height:438px;overflow:hidden;background:var(--bg)}
body{font-family:"Open Sans",Arial,sans-serif;color:var(--ink)}
.canvas{position:relative;width:1200px;height:438px;overflow:hidden;background:radial-gradient(ellipse at 50% 40%,var(--bg) 0%,var(--bg-dark) 100%)}
.abs{position:absolute}
.brand{display:flex;align-items:center;gap:5px}
.brand-mark{background:var(--blue);flex:none}
.brand-name{font-family:"Exo 2",Arial,sans-serif;font-weight:700;color:var(--blue);text-transform:uppercase;line-height:1;white-space:nowrap}
.hero-brand{left:24px;top:84px;gap:7px}
.hero-brand .brand-mark{width:38px;height:38px}
.hero-brand .brand-name{font-size:17px;line-height:1.05;white-space:normal;width:130px}
.section-title{left:48px;top:148px;font-size:10px;color:var(--label)}
.label{font-size:6px;color:var(--label);text-align:center}
.card{background:var(--paper);box-shadow:0 2px 5px rgba(0,0,0,.5);overflow:hidden}
.card-front{left:24px;top:174px;width:168px;height:94px;padding:10px 8px;font-size:4.3px;line-height:1.45}
.card-front .name{font-weight:600;font-size:5px}
.card-front .side{position:absolute;right:10px;top:40px}
.card-front .side .brand-mark{width:8px;height:8px}
.card-front .side .brand-name{font-size:5px}
.card-back{left:24px;top:298px;width:168px;height:104px;display:flex;align-items:center;justify-content:center}
.card-back .brand-mark{width:14px;height:14px}
.card-back .brand-name{font-size:8px}
.letterhead{top:20px;width:286px;height:370px;background:linear-gradient(180deg,var(--paper) 0%,var(--paper-shade) 100%)}
.lh-a{left:206px}.lh-b{left:504px}
.letterhead .brand{position:absolute;left:12px;top:12px}
.letterhead .brand-mark{width:12px;height:12px}
.letterhead .brand-name{font-size:7px}
.lh-address,.lh-contact{position:absolute;top:12px;font-size:3.6px;line-height:1.5}
.lh-address{left:120px}.lh-contact{left:196px}
.lh-decor{position:absolute;left:72px;top:110px;width:140px;height:140px;background:radial-gradient(circle at 40% 40%,var(--blue-pale) 0%,rgba(214,238,249,0) 70%)}
.lh-band{position:absolute;left:0;right:0;bottom:0;height:8px;background:linear-gradient(90deg,var(--blue-deep),var(--blue))}
.lh-b .lh-band{height:12px;font-size:3.6px;color:#fff;text-align:center;line-height:12px}
.envelope{width:352px;overflow:hidden;box-shadow:0 2px 5px rgba(0,0,0,.5)}
.env-1{left:822px;top:20px;height:110px;background:var(--env-dark)}
.env-2{left:822px;top:98px;height:118px;background:var(--paper)}
.env-3{left:822px;top:178px;height:150px;background:var(--paper)}
.env-4{left:808px;top:262px;height:128px;width:322px;background:var(--paper)}
.envelope svg.flap{position:absolute;left:0;top:0}
.env-1 .brand{position:absolute;left:158px;top:30px;flex-direction:column;gap:4px}
.env-1 .brand-mark{width:20px;height:20px;background:#e8e9ea}
.env-1 .brand-name{font-size:4px;color:#e8e9ea}
.env-4 .brand{position:absolute;left:12px;top:14px}
.env-4 .brand-mark{width:12px;height:12px}
.env-4 .brand-name{font-size:7px}
.env-4 .return{position:absolute;left:12px;top:32px;font-size:3.6px;line-height:1.5}
.env-4 .band{position:absolute;left:0;right:0;bottom:0;height:5px;background:var(--blue)}
.lab-lh-a{left:206px;top:404px;width:286px}
.lab-lh-b{left:504px;top:404px;width:286px}
.lab-env{left:822px;top:404px;width:352px}
.lab-front{left:24px;top:273px;width:168px}
.lab-back{left:24px;top:408px;width:168px}
</style>
</head>
<body>
<main class="canvas">
  <div class="abs brand hero-brand"><span class="brand-mark"></span><span class="brand-name">Veracor IT<br>Systems</span></div>
  <p class="abs section-title">Stationery Concepts</p>

  <section class="abs card card-front">
    <p class="name">Martin Osgood</p>
    <p>Vice President</p>
    <p>Veracor IT Systems</p>
    <p>Harbourline Tower</p>
    <p>482 Dunmore Ave East,Suite 3100</p>
    <p>Toronto ON, M4R 2T7</p>
    <p>martin.osgood@veracorsystems-example.ca</p>
    <p>www.veracorsystems-example.ca</p>
    <div class="brand side"><span class="brand-mark"></span><span class="brand-name">Veracor</span></div>
  </section>
  <p class="abs label lab-front">Front Card</p>
  <section class="abs card card-back">
    <div class="brand"><span class="brand-mark"></span><span class="brand-name">Veracor Systems</span></div>
  </section>
  <p class="abs label lab-back">Back Card</p>

  <section class="abs letterhead lh-a">
    <div class="brand"><span class="brand-mark"></span><span class="brand-name">Veracor IT Systems</span></div>
    <div class="lh-address"><p>Harbourline Tower</p><p>482 Dunmore Ave East,Suite 3100</p><p>Toronto ON, M4R 2T7</p></div>
    <div class="lh-contact"><p>T: 416.555.0148</p><p>martin.osgood@veracorsystems-example.ca</p><p>www.veracorsystems-example.ca</p></div>
    <div class="lh-decor" role="img" aria-label="Faint brand watermark area"></div>
    <div class="lh-band"></div>
  </section>
  <p class="abs label lab-lh-a">Letterhead Concept A</p>

  <section class="abs letterhead lh-b">
    <div class="brand"><span class="brand-mark"></span><span class="brand-name">Veracor IT Systems</span></div>
    <div class="lh-address"><p>Harbourline Tower</p><p>482 Dunmore Ave East,Suite 3100</p><p>Toronto ON, M4R 2T7</p></div>
    <div class="lh-contact"><p>T: 416.555.0148</p><p>F: 416.555.0149</p><p>www.veracorsystems-example.ca</p></div>
    <div class="lh-decor" role="img" aria-label="Faint brand watermark area"></div>
    <div class="lh-band">www.veracorsystems-example.ca</div>
  </section>
  <p class="abs label lab-lh-b">Letterhead Concept B</p>

  <section class="abs envelope env-1">
    <div class="brand"><span class="brand-mark"></span><span class="brand-name">Veracor Systems</span></div>
  </section>
  <section class="abs envelope env-2">
    <svg class="flap" width="352" height="60" viewBox="0 0 352 60">
      <defs><linearGradient id="flapBlue" x1="0" y1="0" x2="0" y2="1"><stop offset="0" stop-color="#1178b0"/><stop offset="1" stop-color="#5cc3ee"/></linearGradient></defs>
      <polygon points="0,0 352,0 176,56" fill="url(#flapBlue)"/>
    </svg>
  </section>
  <section class="abs envelope env-3">
    <svg class="flap" width="352" height="70" viewBox="0 0 352 70">
      <polygon points="0,0 352,0 176,62" fill="#f2f4f6" stroke="#d5d9de" stroke-width="1"/>
    </svg>
  </section>
  <section class="abs envelope env-4">
    <div class="brand"><span class="brand-mark"></span><span class="brand-name">Veracor IT Systems</span></div>
    <div class="return"><p>Harbourline Tower</p><p>482 Dunmore Ave East,Suite 3100</p><p>Toronto ON, M4R 2T7</p></div>
    <div class="band"></div>
  </section>
  <p class="abs label lab-env">Envelope Concepts</p>
</main>
</body>
</html>
```